Disease outbreak warning

I need a flyer that explains to hunters how to act as frontline responders to potential disease outbreaks in wildlife populations. In this case the disease is African Swine Fever. We need an at a glance style with plenty of colour and that’s very easy to read.

I HAVE ATTACHED SOME EXISTING FLYERS FROM OVERSEAS ETC THAT CONTAIN SOME OF THE RELEVANT INFO. THEY ARE TO BE USED AS A GUIDE ONLY.
Updates

Need to see some more options. We have some that can be developed successfully but we’d like to see some more options that will suit a national campaign.

Target Market(s)

Australian hunters encountering wild pigs. Typical age is from 18 to 32 but can be older. Male or female.

Colors

Designer to choose colors to be used in the design.

Requirements
Must have
• The KVRTE logo (supplied). It should be relatively small at the bottom of the page. Plus we need room for two or three other logos that can be overprinted on the project if required.
• Must have information for hunters as the main focus.
Nice to have
• A double sided flyer.
Should not have
• US spelling.

```html
<!DOCTYPE html>
<html lang="en-AU">
<head>
<meta charset="utf-8">
<title>African Swine Fever – Advice for Hunters</title>
<link rel="stylesheet" href="https://fonts.googleapis.com/css2?family=Tinos:ital,wght@0,400;0,700;1,700&display=swap">
<style>
  :root{
    --navy:#1c2350;
    --green:#2f9a3a;
    --green-dark:#1f7a2a;
    --white:#ffffff;
    --paper:#f6f7f2;
    --grey:#9a9a9a;
    --sign-red:#c8201e;
  }
  *{margin:0;padding:0;box-sizing:border-box}
  html,body{width:849px;height:1200px;overflow:hidden;background:var(--paper)}
  body{font-family:"Tinos","Times New Roman",serif;color:var(--navy)}
  .flyer{position:relative;width:849px;height:1200px;overflow:hidden;background:var(--paper)}

  .scene-photo{position:absolute;left:0;top:400px;width:849px;height:800px;
    background:linear-gradient(180deg,#c9cbb8 0%,#a79d7a 35%,#7b6a4a 70%,#5b4b33 100%)}
  .pig-hill{position:absolute;left:620px;top:160px;width:229px;height:210px;
    background:radial-gradient(ellipse at 50% 85%,#3f9a3a 0%,#5bb047 55%,rgba(246,247,242,0) 72%)}
  .hunter-art{position:absolute;left:28px;top:820px;width:320px;height:320px;
    background:radial-gradient(ellipse at 50% 55%,#4e6b3a 0%,#6d7f4c 45%,rgba(120,105,75,0) 72%)}

  .intro{position:absolute;left:30px;top:12px;width:760px;font-weight:700;font-size:24px;line-height:28px}
  .intro ul{list-style:none}
  .intro li::before{content:"• "}
  .intro .indent{padding-left:14px}

  .banner{position:absolute;color:var(--white);font-weight:700;font-style:italic;font-size:42px;
    background:var(--green);display:flex;align-items:center}
  .banner-do{left:0;top:425px;width:275px;height:56px;padding-left:40px;
    clip-path:polygon(0 0,88% 0,100% 50%,88% 100%,0 100%)}
  .banner-dont{left:480px;top:645px;width:369px;height:56px;padding-left:50px;
    clip-path:polygon(10% 0,100% 0,100% 100%,10% 100%,0 50%)}

  .list{position:absolute;list-style:none;background:var(--green);color:var(--white);
    font-weight:700;font-size:22px;line-height:26px;padding:10px 18px}
  .list li{margin-bottom:10px}
  .list-do{left:0;top:487px;width:490px;height:150px;padding-left:40px;
    clip-path:polygon(0 0,92% 0,100% 50%,92% 100%,0 100%)}
  .list-dont{left:212px;top:708px;width:637px;height:158px;padding-left:70px;
    clip-path:polygon(7% 0,100% 0,100% 100%,7% 100%,0 50%)}

  .side-strip{position:absolute;right:0;top:930px;width:30px;height:270px;background:var(--grey)}
  .sign-panel{position:absolute;left:690px;top:1058px;width:130px;height:118px;background:var(--white);
    display:flex;align-items:center;justify-content:center}

  .brand{position:absolute;left:16px;top:1075px;display:flex;align-items:center;gap:10px}
  .brand-dot{width:118px;height:118px;border-radius:50%;background:var(--white)}
  .brand-name{position:absolute;left:0;width:118px;text-align:center;font-weight:700;font-size:24px;color:var(--navy)}
</style>
</head>
<body>
<main class="flyer">
  <div class="scene-photo" role="img" aria-label="Photograph of a wild pig lying in dry grassland"></div>
  <div class="pig-hill" role="img" aria-label="Illustration of a wild boar standing on a grassy hill with a tree"></div>
  <div class="hunter-art" role="img" aria-label="Illustration of a hunter aiming a rifle with two dogs"></div>

  <section class="intro">
    <p>The epidemiology of ASF is complex and varies depending on the environment, types of pig production systems, the presence/absence of competent tick vectors, human behaviour, and the presence/absence of wild pigs.</p>
    <p>Routes of transmission can include:</p>
    <ul>
      <li>Direct contact with infected domestic or wild pigs;</li>
      <li>Indirect contact, through ingestion of contaminated material<br><span class="indent">(e.g. food waste, feed, or garbage);</span></li>
      <li>Contaminated fomites, or biological vectors<br><span class="indent">(soft ticks of the genus Ornithodoros) where present.</span></li>
    </ul>
  </section>

  <h2 class="banner banner-do">DO</h2>
  <ul class="list list-do">
    <li>Clean and disinfect all equipment on site.</li>
    <li>Clean and bag all car cases before leaving the hunting area.</li>
    <li>Report any signs of sick or dead pigs.</li>
  </ul>

  <h2 class="banner banner-dont">Don't</h2>
  <ul class="list list-dont">
    <li>Leave leftovers from your meals in the hunting area.</li>
    <li>Hunt wild pigs if you are in contact with domestic pigs.</li>
    <li>Travel with uncovered or unbagged carcasses in the back of a ute.</li>
  </ul>

  <div class="side-strip"></div>
  <div class="sign-panel">
    <svg width="96" height="96" viewBox="0 0 96 96" role="img" aria-label="No pigs sign">
      <ellipse cx="48" cy="52" rx="24" ry="14" fill="#222"/>
      <circle cx="48" cy="48" r="42" fill="none" stroke="var(--sign-red)" stroke-width="8"/>
      <line x1="18" y1="18" x2="78" y2="78" stroke="var(--sign-red)" stroke-width="8"/>
    </svg>
  </div>

  <div class="brand">
    <div class="brand-dot"></div>
    <span class="brand-name">KVRTE</span>
  </div>
</main>
</body>
</html>
```